flyer for letter box drop 2012

Advertising flyer that is delivered to homes in our suburb.
We are optometrists and looking to have a flyer delivered into our local area residential letterboxes. As a business that has been in the area for 25 years we are looking for an innovative approach to keeping our existing customers as well as appealing to the new generation.
We would like the flyer to reflect or professional eye care services
and commitment to quality service and products.
We do not promote our selves as a discount outlet for eg 2 for 1,50% of everything.
I have attached a copy of the flyer we have been using for the last 12 months.

Reason: Away for 3 days

Reason: advertising manager on leave for 7 days, still to review designs

25- 70 year olds male and female

Residential

• flyer should be double sided a5 page
Prominent logo display
address ,phone number , web address,

```html
<!DOCTYPE html>
<html lang="en">
<head>
<meta charset="utf-8">
<title>Larkin Lane Optical – Flyer</title>
<link rel="stylesheet" href="https://fonts.googleapis.com/css2?family=Source+Sans+3:wght@400&display=swap">
<style>
  :root {
    --navy: #2b2f7a;
    --white: #ffffff;
    --panel-top: #5eaadc;
    --panel: #76bfea;
    --violet-1: #b9b6d6;
    --violet-2: #7d7bb0;
    --violet-3: #4f4d8d;
    --violet-4: #3b3f8b;
    --green-1: #e6f0e2;
    --green-2: #c9e1c1;
    --green-3: #a6cf9c;
    --green-4: #7dba75;
    --green-5: #55a652;
    --green-6: #2f9a3e;
    --photo-warm: #d6bca6;
    --photo-pale: #ebe9e5;
  }
  html, body {
    margin: 0;
    padding: 0;
    overflow: hidden;
    background: var(--white);
  }
  .flyer {
    position: relative;
    width: 776px;
    height: 1200px;
    overflow: hidden;
    background: var(--white);
    font-family: "Source Sans 3", "Myriad Pro", sans-serif;
  }
  .backdrop {
    position: absolute;
    inset: 0;
  }
  .brand {
    position: absolute;
    left: 33px;
    top: 22px;
    margin: 0;
    color: var(--navy);
    font-weight: 400;
    line-height: 1;
  }
  .brand__line {
    display: block;
  }
  .brand__line--top {
    font-size: 58px;
    letter-spacing: -0.5px;
  }
  .brand__line--bottom {
    font-size: 126px;
    letter-spacing: -2px;
    margin-top: -8px;
    margin-left: 24px;
  }
  .message {
    position: absolute;
    left: 69px;
    right: 0;
    top: 755px;
    text-align: center;
    color: var(--white);
    text-shadow: 0 1px 3px rgba(20, 50, 90, 0.55);
  }
  .message__headline {
    margin: 0;
    font-size: 55px;
    font-weight: 400;
    line-height: 60px;
  }
  .message__tagline {
    margin: 0;
    font-size: 42px;
    line-height: 48px;
  }
  .contact {
    margin: 24px 0 0;
    font-style: normal;
    font-size: 33px;
    line-height: 40px;
  }
</style>
</head>
<body>
<main class="flyer">
  <svg class="backdrop" width="776" height="1200" viewBox="0 0 776 1200">
    <defs>
      <clipPath id="above-panel">
        <rect x="0" y="0" width="776" height="310"/>
      </clipPath>
      <linearGradient id="panel-fill" x1="0" y1="0" x2="0" y2="1">
        <stop offset="0" stop-color="var(--panel-top)"/>
        <stop offset="0.35" stop-color="var(--panel)"/>
        <stop offset="1" stop-color="var(--panel)"/>
      </linearGradient>
      <radialGradient id="green-core" cx="0.3" cy="0.5" r="0.7">
        <stop offset="0" stop-color="#7cc043"/>
        <stop offset="1" stop-color="var(--green-6)"/>
      </radialGradient>
      <linearGradient id="photo-fill" gradientUnits="userSpaceOnUse" x1="30" y1="0" x2="755" y2="0">
        <stop offset="0" stop-color="var(--photo-warm)"/>
        <stop offset="1" stop-color="var(--photo-pale)"/>
      </linearGradient>
    </defs>

    <g class="rings-violet" clip-path="url(#above-panel)">
      <circle cx="595" cy="405" r="252" fill="var(--violet-1)"/>
      <circle cx="595" cy="405" r="216" fill="var(--violet-2)"/>
      <circle cx="595" cy="405" r="181" fill="var(--violet-3)"/>
      <circle cx="595" cy="405" r="142" fill="var(--violet-4)"/>
    </g>

    <g class="rings-green">
      <circle cx="50" cy="1215" r="498" fill="var(--green-1)"/>
      <circle cx="50" cy="1215" r="436" fill="var(--green-2)"/>
      <circle cx="50" cy="1215" r="374" fill="var(--green-3)"/>
      <circle cx="50" cy="1215" r="312" fill="var(--green-4)"/>
      <circle cx="50" cy="1215" r="250" fill="var(--green-5)"/>
      <circle cx="50" cy="1215" r="180" fill="url(#green-core)"/>
    </g>

    <path class="panel" d="M69 309 H776 V1022 H97 Q69 1022 69 994 Z" fill="url(#panel-fill)" opacity="0.97"/>

    <g class="hero-photo" role="img" aria-label="Photograph: a woman wearing dark oval glasses beside a blurred eye-test letter chart" fill="url(#photo-fill)">
      <circle cx="250" cy="500" r="220"/>
      <circle cx="595" cy="586" r="160"/>
    </g>
  </svg>

  <h1 class="brand">
    <span class="brand__line brand__line--top">Larkin Lane</span>
    <span class="brand__line brand__line--bottom">optical</span>
  </h1>

  <section class="message">
    <h2 class="message__headline">Independent Optometrists</h2>
    <p class="message__tagline">Servicing Ashdale Since 1989</p>
    <address class="contact">
      14b Larkin Lane Westbrook<br>
      Tel: 9315 0284<br>
      www.larkinlaneoptical.com.au
    </address>
  </section>
</main>
</body>
</html>
```